Geschäftspapiere für Termin Startup
Zielgruppe
Wir sind ein Startup, das über die Seite Planorix.de (derzeit noch in der Beta-Phase)zukünftig folgenden Service anbietet: Unternehmer können sehr flexibel (selbst) gestaltete Terminformulare erstellen und auf Ihrer Website einbinden. Kunden können dann diese Termine buchen und bekommen dann Erinnerungs-Mails und SMS.
Zielgruppe: Dienstleister wie Fotografen, Friseure, Versicherungsvertreter, Masseure, Restaurants, Arztpraxen. Also alle, die darauf angewiesen sind, dass vereinbarte Termine eingehalten werden und die die Terminvereinbarung vereinfachen wollen. Also weniger per Telefon, mehr über die eigene Website.
Dateien bitte beachten für die Ansicht des Look & Feels:
https://ablage.beispielwolke.de/open?id=7QmrtHkWz2LpA94bNc3sVyTeOx8dGJuR_
Bonus-Aktion: Wir zahlen pauschal jeweils 30,00 Euro an die Designer auf den Plätzen 2 bis 4 für die geleistete Arbeit. Nur einer kann gewinnen und den Zuschlag bekommen. Aber so möchten wir gerne die Arbeit dennoch honorieren.
Aufgabenstellung
Wir benötigen ein modernes Briefpapier-Layout passend zu unserem CD.
Gerne darf/soll der ORBO (siehe Maskottchen in https://ablage.beispielwolke.de/open?id=5PwqNsYt8BaLmr2Hc7xkDuQOEPfjWzVbn )darauf erscheinen.
Maskottchen ORBO gibt es in mehreren Varianten. Siehe https://ablage.beispielwolke.de/ordner/8TrnWqLeHd5XcmZ3sJ4yPvBkGfQaNuRox?teilen=ja
Auch als Variante, das Maskottchen ORBO gegen das Logo gelehnt ist, kann genutzt werden: https://ablage.beispielwolke.de/open?id=3MuxBgTpW7RkaNj6yVqLeDsHcZoPfGtYi
Das Thema 'Terminvereinbarung' soll sofort erfasst werden mittels des Layouts bzw. der grafischen Elemente.
Auch die Branchen-Icons ( https://ablage.beispielwolke.de/ordner/6HpvRtNmQ2WkzLx8yEcBaJdFsUoGiTbeq?teilen=ja ) dürfen verwendet werden.

```html
<!DOCTYPE html>
<html lang="de">
<head>
<meta charset="utf-8">
<title>Planorix Briefpapier</title>
<link href="https://fonts.googleapis.com/css2?family=Cabin:wght@400;600;700&display=swap" rel="stylesheet">
<style>
  :root{
    --green:#8dc63f;
    --text:#5b6168;
    --text-dark:#4c535b;
    --footer:#858c93;
    --stripe-red:#e03a3a;
    --stripe-yellow:#f6c21c;
    --ring:#ececec;
    --paper:#ffffff;
  }
  *{box-sizing:border-box;margin:0;padding:0}
  html,body{width:848px;height:1200px;overflow:hidden;background:var(--paper)}
  body{font-family:"Cabin",sans-serif;color:var(--text);position:relative}
  .sheet{position:relative;width:848px;height:1200px;overflow:hidden}

  .backdrop-ring{position:absolute;left:0;top:0;width:848px;height:1200px;z-index:0}
  .sheet > *:not(.backdrop-ring){z-index:1}

  .header-rule{position:absolute;top:76px;height:2px;background:var(--green)}
  .header-rule.left{left:0;width:284px}
  .header-rule.right{left:592px;width:256px}
  .brand{position:absolute;left:292px;top:50px;width:292px;height:60px}
  .brand-mark{position:absolute;left:0;top:10px;width:36px;height:36px;background:var(--green)}
  .brand-name{position:absolute;left:46px;top:2px;font-size:44px;font-weight:700;color:var(--green);line-height:50px;letter-spacing:-.5px}
  .brand-tag{position:absolute;right:0;top:50px;font-size:12px;color:var(--text)}

  .sender-line{position:absolute;left:100px;top:173px;font-size:10.5px;color:var(--text)}
  .sender-line b{font-weight:600}

  .recipient{position:absolute;left:100px;top:201px;font-size:14px;line-height:19px;color:var(--text-dark);font-style:normal}

  .contact{position:absolute;left:504px;top:201px;font-size:13.5px;line-height:18px;color:var(--text-dark)}
  .contact b{font-weight:600}
  .contact p{margin-bottom:13px}

  .subject{position:absolute;left:100px;top:392px;font-size:16px;font-weight:700;color:var(--text-dark)}

  .letter{position:absolute;left:100px;top:456px;width:632px;font-size:12.9px;line-height:19.2px;letter-spacing:-.1px;color:var(--text-dark);hyphens:auto}
  .letter p{margin-bottom:11px}
  .letter .salutation{margin-bottom:12px}

  .closing{position:absolute;left:100px;top:866px;font-size:13.3px;color:var(--text-dark)}
  .signature{position:absolute;left:102px;top:886px;width:52px;height:20px;background:linear-gradient(90deg,#3c3f44,#8a8f95);opacity:.5;border-radius:3px}
  .signer{position:absolute;left:100px;top:920px;font-size:9.5px;line-height:13px;color:var(--text-dark)}

  .mascot{position:absolute;left:588px;top:886px;width:228px;height:192px;border-radius:50% 50% 8px 8px;background:radial-gradient(ellipse at 50% 45%,#9ccd52 0%,#8dc63f 40%,#b9bdc2 100%)}

  .footer-stripe{position:absolute;top:1078px;height:3px}
  .footer-stripe.green{left:0;width:374px;background:var(--green)}
  .footer-stripe.red{left:374px;width:191px;background:var(--stripe-red)}
  .footer-stripe.yellow{left:565px;width:283px;background:var(--stripe-yellow)}
  .footer{position:absolute;left:0;top:1081px;width:848px;height:119px;background:var(--footer);color:#fff;font-size:10px;line-height:15px}
  .footer-col{position:absolute;top:17px}
  .footer-col b{font-weight:600}
  .footer-col .accent{color:var(--green)}
  .col-company{left:100px}
  .col-legal{left:226px}
  .col-bank{left:413px}
  .col-contact{left:595px}
</style>
</head>
<body>
<div class="sheet">
  <svg class="backdrop-ring" viewBox="0 0 848 1200" aria-hidden="true">
    <circle cx="850" cy="1170" r="440" fill="none" stroke="var(--ring)" stroke-width="56"/>
  </svg>

  <div class="header-rule left"></div>
  <div class="header-rule right"></div>
  <div class="brand">
    <span class="brand-mark"></span>
    <span class="brand-name">Planorix</span>
    <span class="brand-tag">Tool by datumwerk-beispiel.com</span>
  </div>

  <div class="sender-line"><b>Planorix GmbH</b> | Musterstraße 23 | 12345 Musterhausen</div>

  <address class="recipient">
    Friseursalon Lockenwerk<br>
    Frau Lena Brodt<br>
    Lindenhof 9<br>
    10117 Berlin
  </address>

  <div class="contact">
    <p><b>Ansprechpartner:</b> Jonas Kettler</p>
    <p><b>Abteilung:</b> Kundenservice</p>
    <p><b>Telefon:</b> 04521 - 73 19 40 -12<br>
       <b>Telefax:</b> 04521 - 73 19 40 -134<br>
       <b>E-Mail:</b>&nbsp; j.kettler@planorix.de</p>
    <p><b>Datum:</b>&nbsp; 24. Juni 2018</p>
  </div>

  <h1 class="subject">Betreffzeile Lorem ipsum dolor sit amet</h1>

  <div class="letter">
    <p class="salutation">Sehr geehrte Frau Brodt,</p>
    <p>lorem ipsum dolor sit amet, consetetur sadipscing elitr, sed diam nonumy eirmod tempor invidunt ut labore et dolore magna aliquyam erat, sed diam voluptua. At vero eos et accusam et justo duo dolores et ea rebum. Stet clita kasd gubergren, no sea takimata sanctus est Lorem ipsum dolor sit amet. Lorem ipsum dolor sit amet, consetetur sadipscing elitr, sed diam nonumy eirmod tempor invidunt ut labore et dolore magna aliquyam erat, sed diam voluptua. At vero eos et accusam et justo duo dolores et ea rebum. Stet clita kasd gubergren, no sea takimata sanctus est Lorem ipsum dolor sit amet. Lorem ipsum dolor sit amet, consetetur sadipscing elitr, sed diam nonumy eirmod tempor invidunt ut labore et dolore magna aliquyam erat, sed diam voluptua. At vero eos et accusam et justo duo dolores et ea rebum. Stet clita kasd gubergren, no sea takimata sanctus est Lorem ipsum dolor sit amet.</p>
    <p>Duis autem vel eum iriure dolor in hendrerit in vulputate velit esse molestie consequat, vel illum dolore eu feugiat nulla facilisis at vero eros et accumsan et iusto odio dignissim qui blandit praesent luptatum zzril delenit augue duis dolore te feugait nulla facilisi. Lorem ipsum dolor sit amet, consectetuer adipiscing elit, sed diam nonummy nibh euismod tincidunt ut laoreet dolore magna aliquam erat volutpat.</p>
    <p>Ut wisi enim ad minim veniam, quis nostrud exerci tation ullamcorper suscipit lobortis nisl ut aliquip ex ea commodo consequat. Duis autem vel eum iriure dolor in hendrerit in vulputate velit esse molestie consequat, vel illum dolore eu feugiat nulla facilisis at vero eros et accumsan et iusto odio dignissim qui blandit praesent luptatum zzril delenit augue duis dolore te feugait nulla facilisi.</p>
  </div>

  <div class="closing">Mit freundlichen Grüßen,</div>
  <div class="signature" role="img" aria-label="Handschriftliche Unterschrift"></div>
  <div class="signer">Jonas Kettler<br>Projektmanager</div>

  <div class="mascot" role="img" aria-label="Maskottchen ORBO mit Zauberhut und Zauberstab"></div>

  <div class="footer-stripe green"></div>
  <div class="footer-stripe red"></div>
  <div class="footer-stripe yellow"></div>
  <footer class="footer">
    <div class="footer-col col-company"><b class="accent">Planorix GmbH</b><br>Musterstraße 23<br>12345 Musterhausen</div>
    <div class="footer-col col-legal">Geschäftsführer: Rainer Wollmann<br>Handelsregister Musterhausen<br>Musterhausener Bank<br>IBAN: DE44 5002 1094 8830 17<br>BIC: PLNXDEB1XXX</div>
    <div class="footer-col col-bank"><b>Bankverbindung</b><br>IBAN: DE44 5002 1094 8830 17<br>BIC: PLNXDEB1XXX<br>USt-IdNr: DE31847260</div>
    <div class="footer-col col-contact"><b>Kontakt</b><br>Telefon: 04521 - 73 19 40 0<br>Telefax: 04521 - 73 19 40 - 134<br>E-Mail: info@planorix.de<br>Webseite: www.planorix.de</div>
  </footer>
</div>
</body>
</html>
```